Oversized Postcard Designer

Oversized( 8.52 by 4.57) handout postcards.
We need promotional post cards that our congregation can use to pass out to their frineds and family for a special Harvest Light Gathering. I attempted to create "something" but was not completely satisfied with it. I have included my attempt in the uploaded images.
Trhe front part of the post card I would like for it to capture the attention of people. The Backside of the postcard can contain event information.
About the Event Information.
Harvest Light Gathering
Special Guest: Dale Whitcombe (www.dalewhitcombe-example.org)
Dates: Sunday March 15 thru Wednesday March 18
Times: Sunday 9:00 a.m., 11:00 a.m., and 6:00 p.m.
Monday - Wednesday 6:00 p.m. with a free meal being served at 5:00 p.m.
Our Location is 418 N. Larch Street, Independence, KS 60000
Our Phone Number 555-482-1937

```html
<!DOCTYPE html>
<html lang="en">
<head>
<meta charset="utf-8">
<title>Harvest Light Gathering – Postcard</title>
<link rel="stylesheet" href="https://fonts.googleapis.com/css2?family=Cinzel:wght@400;700&family=Cinzel+Decorative:wght@700&display=swap">
<style>
  :root {
    --page: #ffffff;
    --navy: #1d3f7a;
    --band-deep: #0b2c5e;
    --band-mid: #1c5aa6;
    --band-light: #3a86d1;
    --sky-top: #d9e9f7;
    --sky-low: #9ec3e6;
    --stone: #8d8a84;
    --duo-deep: #123e6e;
    --duo-mid: #2f6ea8;
    --duo-light: #6aa3d4;
    --accent: #f29a2e;
    --white: #ffffff;
  }
  * { box-sizing: border-box; margin: 0; padding: 0; }
  html, body { width: 1200px; height: 1000px; overflow: hidden; background: var(--page); }
  body { position: relative; font-family: "Cinzel", serif; }

  .card {
    position: absolute; left: 250px; width: 710px; height: 459px;
    overflow: hidden; box-shadow: 0 3px 10px rgba(0,0,0,.35);
  }
  .card--front { top: 35px; }
  .card--back  { top: 518px; }

  /* Front */
  .front-photo {
    position: absolute; inset: 0;
    background:
      radial-gradient(ellipse 45% 55% at 40% 50%, rgba(230,220,200,.85), transparent 70%),
      linear-gradient(180deg, var(--sky-top) 0%, var(--white) 35%, var(--sky-low) 65%, var(--stone) 78%);
  }
  .front-band { position: absolute; left: 0; top: 0; width: 710px; height: 459px; }
  .front-brand {
    position: absolute; left: 28px; top: 24px;
    font-size: 17px; font-weight: 700; color: #222; display: flex; align-items: center; gap: 8px;
  }
  .front-brand .mark { width: 28px; height: 28px; border-radius: 50%; background: #222; }
  .front-story {
    position: absolute; left: 456px; top: 80px; width: 240px;
    color: var(--navy); font-size: 16.5px; line-height: 1.42; font-variant: small-caps;
  }
  .front-story p + p { margin-top: 10px; }
  .front-church {
    position: absolute; left: 462px; top: 268px; width: 125px;
    display: flex; flex-direction: column; align-items: center; gap: 8px;
    color: var(--white); font-size: 15px; line-height: 1.1; text-align: center;
  }
  .front-church .mark { width: 26px; height: 26px; background: var(--band-mid); }
  .event-kicker { position: absolute; left: 36px; top: 344px; color: var(--white); font-size: 19px; }
  .event-title {
    position: absolute; left: 34px; top: 362px; color: var(--white);
    font-family: "Cinzel Decorative", serif; font-size: 40px; font-weight: 700;
  }
  .event-guest { position: absolute; left: 38px; top: 422px; color: var(--white); font-size: 13px; }
  .event-guest strong { font-size: 18px; font-weight: 400; font-style: italic; margin-left: 12px; }
  .event-dates { position: absolute; right: 16px; top: 420px; color: var(--white); font-size: 19px; }
  .event-dates sup { font-size: 11px; }

  /* Back */
  .back-photo {
    position: absolute; inset: 0;
    background:
      radial-gradient(ellipse 30% 45% at 22% 55%, var(--duo-light), transparent 75%),
      linear-gradient(120deg, var(--duo-mid) 0%, var(--duo-deep) 55%, #0d2f57 100%);
  }
  .back-brand {
    position: absolute; left: 32px; top: 24px; display: flex; align-items: center; gap: 8px;
    color: rgba(255,255,255,.55); font-size: 17px; font-weight: 700;
  }
  .back-brand .mark { width: 28px; height: 28px; border-radius: 50%; background: rgba(255,255,255,.35); }
  .back-church {
    position: absolute; left: 30px; top: 395px; display: flex; align-items: center; gap: 10px;
    color: rgba(255,255,255,.6); font-size: 17px; line-height: 1.1;
  }
  .back-church .mark { width: 38px; height: 38px; background: rgba(255,255,255,.3); }
  .back-info {
    position: absolute; left: 300px; top: 24px; width: 340px; text-align: center; color: var(--white);
  }
  .back-info .kicker { font-size: 19px; }
  .back-info .title { font-family: "Cinzel Decorative", serif; font-size: 40px; font-weight: 700; line-height: 1; margin-top: 2px; }
  .back-info .guest-label { color: var(--accent); font-size: 12px; margin-top: 22px; }
  .back-info .guest-feature { color: var(--accent); font-size: 15px; margin-top: 2px; }
  .back-info .guest-name { color: var(--accent); font-size: 19px; font-style: italic; }
  .back-info .story { font-size: 11.4px; line-height: 1.72; margin-top: 20px; }
  .back-info .times { color: var(--accent); font-size: 11.4px; line-height: 1.4; margin-top: 20px; }
  .back-info .address { font-size: 12px; margin-top: 16px; }
  .back-info .phone { font-size: 14px; margin-top: 2px; }
</style>
</head>
<body>

<section class="card card--front">
  <div class="front-photo" role="img" aria-label="Photo of the guest speaker seated on a stone wall, hands folded in prayer, against a bright cloudy sky"></div>
  <svg class="front-band" viewBox="0 0 710 459" aria-hidden="true">
    <defs>
      <linearGradient id="bandFill" x1="0" y1="0" x2="0" y2="1">
        <stop offset="0" stop-color="#1c5aa6"/>
        <stop offset="1" stop-color="#0b2c5e"/>
      </linearGradient>
      <pattern id="bandStripe" width="8" height="8" patternUnits="userSpaceOnUse" patternTransform="rotate(45)">
        <rect width="4" height="8" fill="rgba(255,255,255,.05)"/>
      </pattern>
    </defs>
    <polygon points="0,352 100,300 520,405 710,330 710,459 0,459" fill="#3a86d1"/>
    <polygon points="0,362 100,312 520,415 710,342 710,459 0,459" fill="url(#bandFill)"/>
    <polygon points="0,362 100,312 520,415 710,342 710,459 0,459" fill="url(#bandStripe)"/>
  </svg>
  <div class="front-brand"><span class="mark"></span>Dale Whitcombe Ministries</div>
  <div class="front-story">
    <p>He had nine step-fathers, an alcoholic mother, was abused &amp; neglected, left without hope.</p>
    <p>Until ....</p>
  </div>
  <div class="front-church"><span class="mark"></span>Cornerstone Fellowship Independence</div>
  <div class="event-kicker">Harvest Light</div>
  <div class="event-title">Gathering</div>
  <div class="event-guest">featuring <strong>Dale Whitcombe</strong></div>
  <div class="event-dates">On March 15<sup>th</sup> – 18<sup>th</sup></div>
</section>

<section class="card card--back">
  <div class="back-photo" role="img" aria-label="Blue-toned portrait photo of the smiling guest speaker in a white shirt"></div>
  <div class="back-brand"><span class="mark"></span>Dale Whitcombe Ministries</div>
  <div class="back-church"><span class="mark"></span>Cornerstone Fellowship<br>Independence</div>
  <div class="back-info">
    <div class="kicker">Harvest Light</div>
    <div class="title">Gathering</div>
    <div class="guest-label">Special Guest:</div>
    <div class="guest-feature">Featuring</div>
    <div class="guest-name">Dale Whitcombe</div>
    <p class="story">Despite a horrifying childhood, Dale defied all odds with one choice that would change his life forever, his decision to accept Jesus Christ as his personal Savior. With that one choice, Dale's years of mental and physical abuse turned a useless mess into a powerful message.</p>
    <p class="times">Sunday 9:00 a.m., 11:00 a.m., 6:00 p.m.<br>Monday – Wednesday 6:00 p.m.<br>(free meal at 5:00 p.m.)</p>
    <p class="address">418 N. Larch Street, Independence, KS 60000</p>
    <p class="phone">Call for details (555) 482-1937</p>
  </div>
</section>

</body>
</html>
```